Design business cards for Vantrelo

I am looking for a clean, crisp and professional business card design. A logo already exists with which to work, which is attached in various formats. The design needs to be print ready. A clear brief is attached - please read it carefully and ensure you can deliver what is required. Looking forward to awarding the prize to a great design and great designer!

```html
<!DOCTYPE html>
<html lang="en">
<head>
<meta charset="utf-8">
<title>Vantrelo Business Card</title>
<link href="https://fonts.googleapis.com/css2?family=Lato:wght@400;700&family=Lora:wght@400&display=swap" rel="stylesheet">
<style>
  :root {
    --backdrop: #ece7e0;
    --card: #ffffff;
    --accent: #e8562a;
    --ink: #2b2b2b;
    --muted: #555555;
    --rule: #3a3a3a;
    --brand-dot: #e8562a;
  }
  * { margin: 0; padding: 0; box-sizing: border-box; }
  html, body {
    width: 1200px; height: 759px; overflow: hidden;
    background: var(--backdrop);
    font-family: "Lato", Arial, sans-serif;
  }
  .canvas { position: relative; width: 1200px; height: 759px; }
  .card {
    position: absolute; top: 224px;
    width: 544px; height: 312px;
    background: var(--card);
    border-radius: 20px;
    box-shadow: 0 2px 6px rgba(0,0,0,0.18);
  }
  .card--front { left: 44px; }
  .card--back { left: 611px; }

  .brand { position: absolute; display: flex; align-items: center; }
  .brand__dot {
    width: 52px; height: 52px; border-radius: 50%;
    background: var(--brand-dot); margin-right: 16px;
  }
  .brand__name {
    font-family: "Lora", Georgia, serif; font-weight: 400;
    font-size: 40px; color: var(--ink); line-height: 1;
  }
  .card--front .brand { left: 20px; top: 122px; }
  .card--back .brand { left: 242px; top: 184px; }

  .divider {
    position: absolute; left: 290px; top: 59px;
    width: 1.5px; height: 194px; background: var(--rule);
  }
  .details { position: absolute; left: 317px; top: 56px; color: var(--muted); }
  .details__name { color: var(--accent); font-weight: 700; font-size: 18.5px; line-height: 22px; }
  .details__role { font-size: 14px; line-height: 18px; }
  .details__address { font-size: 12.5px; line-height: 17px; margin-top: 20px; }
  .contacts { list-style: none; margin-top: 11px; font-size: 12.5px; }
  .contacts li { display: flex; align-items: center; height: 16px; }
  .contacts svg { width: 11px; height: 11px; margin-right: 8px; flex: none; }

  .web {
    position: absolute; left: 336px; top: 269px;
    font-family: "Lora", Georgia, serif;
    font-size: 13px; letter-spacing: 2px; color: var(--muted);
  }
  .web__domain { color: var(--accent); }
</style>
</head>
<body>
<div class="canvas">
  <section class="card card--front">
    <div class="brand">
      <span class="brand__dot"></span>
      <span class="brand__name">Vantrelo</span>
    </div>
    <div class="divider"></div>
    <div class="details">
      <p class="details__name">Marcus Hale</p>
      <p class="details__role">BE(Hons) PhD MIEAust GAICD</p>
      <p class="details__role">Director, Principal Consultant</p>
      <p class="details__address">42 Linden Avenue, Ashwood Park<br>Victoria 3147 Australia</p>
      <ul class="contacts">
        <li><svg viewBox="0 0 12 12"><path d="M2.5 1 L4.5 1 L5.3 3.6 L4 4.6 Q5 7 7.4 8 L8.4 6.7 L11 7.5 L11 9.5 Q10.5 11 9 11 Q1 10 1 3 Q1 1.5 2.5 1 Z" fill="var(--accent)"/></svg>+61 (0)412 555 017</li>
        <li><svg viewBox="0 0 12 12"><rect x="0.5" y="2" width="11" height="8" fill="var(--accent)"/><path d="M1 2.5 L6 6.5 L11 2.5" stroke="#fff" stroke-width="1" fill="none"/></svg>mhale@vantrelo.com.au</li>
        <li><svg viewBox="0 0 12 12"><circle cx="6" cy="6" r="5" fill="none" stroke="var(--accent)" stroke-width="1.4"/><ellipse cx="6" cy="6" rx="2" ry="5" fill="none" stroke="var(--accent)" stroke-width="1"/><line x1="1" y1="6" x2="11" y2="6" stroke="var(--accent)" stroke-width="1"/></svg>www.vantrelo.com.au</li>
        <li><svg viewBox="0 0 12 12"><rect x="0.5" y="0.5" width="11" height="11" rx="1.5" fill="var(--accent)"/></svg>profile.vantrelo.com.au/mhale</li>
        <li><svg viewBox="0 0 12 12"><circle cx="6" cy="6" r="5.5" fill="var(--accent)"/></svg>marcus.hale22</li>
      </ul>
    </div>
  </section>

  <section class="card card--back">
    <div class="brand">
      <span class="brand__dot"></span>
      <span class="brand__name">Vantrelo</span>
    </div>
    <p class="web">www.<span class="web__domain">vantrelo</span>.com.au</p>
  </section>
</div>
</body>
</html>
```